Harborlight Energy Local Letter Drop

I need a compelling and visually appealing flyer to promote our solar installation company in our local area of Boronia Victoria.
Because we are an install company without the overheads of the big solar sales companies, we pride ourselves on being the experts and being able to provide great quality service and products at the best prices anywhere.
In a highly competitive market we need to convey that despite government incentives and feed-in tariff rates being reduced by the government, solar has never been more affordable or economical for families. This is due to the significant fall in solar equipment prices, but this is set to change as international manufacturers start to go out of business. With electricity/utility prices set to rise even further, solar is a perfect option for domestic and commercial use.
I want a leaflet that is grabbing and compels people to ring me for a free, no obligation quotation and in-home energy assessment.
We want to differentiate ourselves from the stand-point of cutting out the middle man and being the local, trusted and expert installers.
We want to protect people from the projected 60% rise in electricity prices over the coming 8 years and allow them to produce their own electricity!

```html
<!DOCTYPE html>
<html lang="en">
<head>
<meta charset="utf-8">
<title>Harborlight Energy – Local Letter Drop</title>
<link rel="stylesheet" href="https://fonts.googleapis.com/css2?family=Open+Sans:wght@400;600;700&display=swap">
<style>
  :root {
    --orange: #f5a01a;
    --orange-deep: #e8900c;
    --gold-light: #f6dc78;
    --ink: #1a1a1a;
    --accent-red: #d9261c;
    --white: #ffffff;
    --photo-dark: #2a1d05;
    --photo-mid: #8a6410;
    --photo-light: #e6b53a;
  }
  * { box-sizing: border-box; margin: 0; padding: 0; }
  html, body { width: 848px; height: 1200px; overflow: hidden; background: var(--white); }
  body { font-family: "Open Sans", Verdana, sans-serif; color: var(--ink); }

  .flyer { position: relative; width: 848px; height: 1200px; overflow: hidden; background: var(--white); }

  /* Header */
  .hero-photo {
    position: absolute; left: 0; top: 0; width: 848px; height: 610px;
    background:
      radial-gradient(ellipse at 85% 15%, rgba(240,200,80,0.9), rgba(240,200,80,0) 55%),
      linear-gradient(160deg, var(--photo-light) 0%, var(--photo-mid) 35%, var(--photo-dark) 70%, #3b2a08 100%);
  }
  .hero-shapes { position: absolute; left: 0; top: 0; width: 848px; height: 610px; }
  .brand {
    position: absolute; left: 62px; top: 92px;
    display: flex; align-items: center; gap: 8px;
    font-size: 22px; font-weight: 700; color: #1c1c1c;
  }
  .brand-dot { width: 22px; height: 22px; border-radius: 50%; background: var(--orange); }
  .tagline {
    position: absolute; right: 25px; top: 26px; text-align: right;
    color: var(--white); font-size: 18px; line-height: 23px;
  }
  .hero-questions {
    position: absolute; left: 0; width: 848px; top: 520px; text-align: center; color: var(--white);
  }
  .hero-questions h1 { font-size: 24px; font-weight: 400; line-height: 30px; }
  .hero-questions p { font-size: 20px; line-height: 25px; }

  /* Body frame */
  .frame {
    position: absolute; left: 9px; right: 11px; top: 606px; bottom: 61px;
    border-left: 1px solid var(--orange); border-right: 2px solid var(--orange);
  }

  .intro { position: absolute; left: 51px; width: 746px; top: 625px; font-size: 15.5px; line-height: 21px; }
  .intro p { text-align: justify; text-align-last: center; }
  .intro .lead { text-align: center; margin-bottom: 16px; }
  .intro .offer { margin-top: 18px; text-align-last: left; }
  .intro .phone { color: var(--accent-red); font-size: 18px; }

  .section-title { position: absolute; color: var(--orange); font-size: 16.5px; font-weight: 400; }
  .chart-title { left: 51px; top: 818px; }
  .prices-title { left: 424px; top: 818px; }

  .bill-chart { position: absolute; left: 40px; top: 850px; width: 350px; height: 250px; }
  .bill-chart text { font-family: "Open Sans", Verdana, sans-serif; font-size: 13px; fill: var(--ink); }

  .price-table {
    position: absolute; left: 424px; top: 870px; width: 372px;
    border-collapse: collapse; font-size: 13.5px;
  }
  .price-table th {
    background: var(--orange); color: var(--white); font-weight: 400; text-align: left;
    padding: 0 10px; height: 37px; line-height: 15px; border: 1px solid var(--white);
  }
  .price-table td {
    padding: 0 10px; height: 38px; line-height: 15px;
    border: 1px solid var(--orange); border-top: 1px solid #e7c26a;
  }
  .price-table tr.is-featured td { background: var(--gold-light); }
  .footnote { position: absolute; left: 424px; top: 1035px; font-size: 11px; }

  .call-to-action {
    position: absolute; left: 0; width: 848px; top: 1098px; text-align: center;
    color: var(--orange); font-size: 20.5px;
  }

  .footer-bar {
    position: absolute; left: 0; bottom: 0; width: 848px; height: 61px;
    background: var(--orange); color: var(--white);
    font-size: 15.5px; line-height: 61px; padding-left: 48px;
  }
</style>
</head>
<body>
<main class="flyer">

  <header>
    <div class="hero-photo" role="img" aria-label="Close-up photograph of rooftop solar panels glowing in golden sunlight"></div>
    <svg class="hero-shapes" viewBox="0 0 848 610" aria-hidden="true">
      <path d="M0,0 H362 C320,100 200,165 0,165 Z" fill="var(--white)"/>
      <path d="M362,0 C320,100 200,165 0,165" fill="none" stroke="var(--orange)" stroke-width="6"/>
      <polygon points="0,610 0,598 422,440 848,574 848,610" fill="var(--white)"/>
      <polygon points="14,610 422,448 848,582 848,610" fill="var(--orange)"/>
    </svg>
    <div class="brand"><span class="brand-dot"></span>Harborlight Energy</div>
    <div class="tagline">The Solar Panel Installers<br>Phone: 1300 555 208</div>
    <div class="hero-questions">
      <h1>Have You Thought About Solar?</h1>
      <p>Are you paying too much for electricity?</p>
      <p>Would you like to reduce or even eliminate your bills?</p>
    </div>
  </header>

  <div class="frame"></div>

  <section class="intro">
    <p class="lead">........ then as your local solar installer, we can help you!</p>
    <p>In the past six years, electricity prices have gone up by more than 93% and are due to increase even further! We have helped thousands of households avoid electricity price hikes….and they have been incredibly happy with the savings. Now we would like to pass these savings on to you.</p>
    <p class="offer">As your local installer we would like to offer you a free, no obligation quote and energy assessment to see how solar can work for you, give us a call today on <span class="phone">1300 555 208</span>.</p>
  </section>

  <h2 class="section-title chart-title">Quarterly Electricity Bill Projections</h2>
  <svg class="bill-chart" viewBox="0 0 350 250" aria-label="Bar chart of quarterly electricity bill projections rising from about $300 in 2004 to about $1,170 in 2022">
    <g stroke="#555" stroke-width="1">
      <line x1="76" y1="10" x2="330" y2="10"/>
      <line x1="76" y1="36.6" x2="330" y2="36.6"/>
      <line x1="76" y1="63.3" x2="330" y2="63.3"/>
      <line x1="76" y1="90" x2="330" y2="90"/>
      <line x1="76" y1="116.6" x2="330" y2="116.6"/>
      <line x1="76" y1="143.3" x2="330" y2="143.3"/>
      <line x1="76" y1="170" x2="330" y2="170"/>
      <line x1="76" y1="196.6" x2="330" y2="196.6"/>
      <line x1="76" y1="10" x2="76" y2="196.6"/>
    </g>
    <g text-anchor="end">
      <text x="68" y="14">$1,400</text>
      <text x="68" y="41">$1,200</text>
      <text x="68" y="67">$1,000</text>
      <text x="68" y="94">$800</text>
      <text x="68" y="121">$600</text>
      <text x="68" y="147">$400</text>
      <text x="68" y="174">$200</text>
      <text x="68" y="201">$-</text>
    </g>
    <g fill="var(--orange)">
      <rect x="86" y="156.6" width="9" height="40"/>
      <rect x="111" y="143.3" width="9" height="53.3"/>
      <rect x="136" y="134" width="9" height="62.6"/>
      <rect x="161" y="120.6" width="9" height="76"/>
      <rect x="186" y="107.3" width="9" height="89.3"/>
      <rect x="211" y="98" width="9" height="98.6"/>
      <rect x="236" y="86" width="9" height="110.6"/>
      <rect x="261" y="75.3" width="9" height="121.3"/>
      <rect x="286" y="63.3" width="9" height="133.3"/>
      <rect x="311" y="40.6" width="9" height="156"/>
    </g>
    <g text-anchor="end">
      <text transform="translate(98 210) rotate(-40)">2004</text>
      <text transform="translate(123 210) rotate(-40)">2006</text>
      <text transform="translate(148 210) rotate(-40)">2008</text>
      <text transform="translate(173 210) rotate(-40)">2010</text>
      <text transform="translate(198 210) rotate(-40)">2013</text>
      <text transform="translate(223 210) rotate(-40)">2014</text>
      <text transform="translate(248 210) rotate(-40)">2016</text>
      <text transform="translate(273 210) rotate(-40)">2018</text>
      <text transform="translate(298 210) rotate(-40)">2020</text>
      <text transform="translate(323 210) rotate(-40)">2022</text>
    </g>
  </svg>

  <h2 class="section-title prices-title">Special Knox Resident Prices</h2>
  <table class="price-table">
    <thead>
      <tr><th style="width:96px">KW</th><th style="width:86px">PRICE</th><th style="width:96px">% off bill</th><th>Pay Back Period</th></tr>
    </thead>
    <tbody>
      <tr><td>1.5</td><td>$1650</td><td>35%</td><td>2 years 10 months</td></tr>
      <tr class="is-featured"><td>3</td><td>$4300</td><td>71%</td><td>3 years 7 months</td></tr>
      <tr><td>5</td><td>$7000</td><td>100%</td><td>4 years 2 months</td></tr>
    </tbody>
  </table>
  <p class="footnote">Figures based on average household energy usage of 17kws/day</p>

  <p class="call-to-action">Start enjoying your savings today!</p>

  <footer class="footer-bar">42 Kestrel Lane, Boronia Vic 3155 | Tel: 1300 555 208 | Email: hello@harborlightenergy.com.au</footer>
</main>
</body>
</html>
```